Verpackungsdesign für Glasprodukte
Super Designvorschläge und in kürzester Zeit ausgearbeitet. Danke für die Unterstützung!
Zielgruppe
Wir sind eine Glaser Handwerksunternehmen die Dienstleistung und Glasprodukte verkaufen, unsere Zielgruppe sind BtoB und BtoC Kunden an die wir hochwertige Produkte für faire Preise anbieten.
Aufgabenstellung
Schlichtes und modernes Design, auf der Vorderseite soll das Logo, innen kommt eine Persönlicher Text und ein Bild von mir

```html
<!DOCTYPE html>
<html lang="de">
<head>
<meta charset="utf-8">
<title>Glaserei Kessler – Faltkarte</title>
<link rel="stylesheet" href="https://fonts.googleapis.com/css2?family=Bebas+Neue&family=Lobster&family=Roboto:wght@300;400;500&display=swap">
<style>
:root{
  --page:#bdbdbd;
  --ink:#1a1a1a;
  --dark:#232122;
  --black:#050505;
  --stone:#ebe8e4;
  --white:#ffffff;
  --muted:#9a918d;
  --text-grey:#8c8583;
  --line:#c9c6c3;
  --gold:#a08a5a;
  --ghost:#f1eeeb;
  --stripe:#7d7b7a;
}
*{margin:0;padding:0;box-sizing:border-box}
html,body{width:686px;height:1200px;overflow:hidden;background:var(--page)}
body{position:relative;font-family:"Roboto",Arial,sans-serif}
.abs{position:absolute}
.section-title{position:absolute;left:32px;font-family:"Lobster",cursive;font-size:21px;color:var(--ink);line-height:1}
.sheet{position:absolute;box-shadow:0 1px 3px rgba(0,0,0,.25);overflow:hidden}

/* outside */
.outside{left:30px;top:43px;width:626px;height:293px;
  background:linear-gradient(90deg,#000 0%,#151515 40%,#1f1f1f 70%,#2e2e2e 100%)}
.outside .bands{position:absolute;inset:0}
.fold{position:absolute;top:0;bottom:0;width:1px;background:rgba(255,255,255,.18)}
.contact{position:absolute;color:#e6e6e6;font-size:5px}
.contact h3{font-weight:400;letter-spacing:.4px;margin-bottom:4px}
.contact ul{list-style:none}
.contact li{display:flex;align-items:center;gap:5px}
.contact svg{width:7px;height:7px;flex:none}
.outside .contact{left:260px;top:256px}
.outside .contact h3{font-size:6.2px;margin-bottom:5px}
.outside .contact li{height:11px}
.glass{position:absolute;left:483px;top:102px;width:145px;height:150px;
  border:1px solid rgba(255,255,255,.75);
  background:linear-gradient(135deg,rgba(255,255,255,.18),rgba(255,255,255,.05) 60%,rgba(255,255,255,.12));
  box-shadow:2px 3px 6px rgba(0,0,0,.5)}
.brand-tile{position:absolute;left:510px;top:123px;width:97px;height:107px;background:var(--white);
  border:2px solid var(--gold);display:flex;align-items:center;justify-content:center;text-align:center}
.brand-name{font-family:"Roboto",Arial,sans-serif;font-weight:300;font-size:11px;letter-spacing:1.6px;color:var(--ink);line-height:1.4;text-transform:uppercase}

/* inside */
.inside{left:32px;top:437px;width:623px;height:294px;background:var(--white)}
.panel{position:absolute;top:0;bottom:0}
.title-light{font-family:"Bebas Neue",sans-serif;color:var(--muted);font-size:17px;letter-spacing:.3px;line-height:1}
.body-copy{font-size:5px;line-height:8.2px;color:var(--text-grey);letter-spacing:.05px}
.photo{background:linear-gradient(160deg,#5a5d62 0%,#2c2d30 45%,#16161a 100%)}
.caption{color:#cfcfcf;font-size:5px;line-height:8px;text-align:right}
.vertical-word{position:absolute;font-family:"Bebas Neue",sans-serif;writing-mode:vertical-rl;transform:rotate(180deg);line-height:1;white-space:nowrap}
.inside .contact h3{font-size:6.5px;color:#e0e0e0;margin-bottom:6px}
.inside .contact li{height:9.7px;font-size:3.8px;color:#cfcfcf}

/* alternative */
.alt{left:30px;top:847px;width:623px;height:290px;background:var(--white)}
.title-bold{font-family:"Bebas Neue",sans-serif;color:var(--black);font-size:18.5px;line-height:19px;letter-spacing:.3px}
.alt .contact{left:19px;top:202px;color:#6f6865}
.alt .contact h3{font-size:8px;font-weight:300;margin-bottom:8px;color:#7b7370}
.alt .contact li{height:11.5px;font-size:5px}
.name-plate{position:absolute;background:var(--black);color:#fff;font-size:5.6px;line-height:7px;text-align:right;padding:3px 6px 0 0}
</style>
</head>
<body>

<svg width="0" height="0" style="position:absolute" aria-hidden="true">
  <defs>
    <symbol id="i-pin" viewBox="0 0 10 10"><path d="M5 9.3C3 7 2 5.4 2 4a3 3 0 0 1 6 0c0 1.4-1 3-3 5.3z" fill="none" stroke="currentColor" stroke-width=".8"/><circle cx="5" cy="4" r="1" fill="none" stroke="currentColor" stroke-width=".8"/></symbol>
    <symbol id="i-globe" viewBox="0 0 10 10"><g fill="none" stroke="currentColor" stroke-width=".7"><circle cx="5" cy="5" r="4"/><ellipse cx="5" cy="5" rx="1.8" ry="4"/><path d="M1 5h8M1.6 3h6.8M1.6 7h6.8"/></g></symbol>
    <symbol id="i-mail" viewBox="0 0 10 10"><g fill="none" stroke="currentColor" stroke-width=".8"><rect x="1" y="2.5" width="8" height="5.5"/><path d="M1 2.5l4 3.2 4-3.2"/></g></symbol>
    <symbol id="i-square" viewBox="0 0 10 10"><rect x="1.5" y="1.5" width="7" height="7" rx="1.5" fill="none" stroke="currentColor" stroke-width=".8"/></symbol>
    <symbol id="i-circle" viewBox="0 0 10 10"><circle cx="5" cy="5" r="4" fill="none" stroke="currentColor" stroke-width=".8"/></symbol>
  </defs>
</svg>

<!-- Außenseite -->
<h2 class="section-title" style="top:9px">Außenseite</h2>
<section class="sheet outside">
  <svg class="bands" viewBox="0 0 626 293" preserveAspectRatio="none" aria-hidden="true">
    <g fill="#ffffff">
      <polygon points="330,0 390,0 140,293 80,293" opacity=".03"/>
      <polygon points="470,0 520,0 270,293 220,293" opacity=".04"/>
      <polygon points="560,0 600,0 360,293 320,293" opacity=".05"/>
      <polygon points="600,0 626,0 626,40 420,293 390,293" opacity=".05"/>
      <polygon points="626,120 626,170 520,293 480,293" opacity=".06"/>
    </g>
  </svg>
  <div class="fold" style="left:211px"></div>
  <div class="fold" style="left:422px"></div>
  <div class="contact">
    <h3>Glaserei Kessler</h3>
    <ul>
      <li><svg><use href="#i-pin"/></svg>Lindenweg 12, 22145 Nordstadt</li>
      <li><svg><use href="#i-globe"/></svg>info@glaserei-kessler.de</li>
      <li><svg><use href="#i-mail"/></svg>www.glaserei-kessler.de</li>
      <li><svg><use href="#i-square"/></svg>XXX Glaserei Kessler</li>
      <li><svg><use href="#i-circle"/></svg>www.netzprofil.de/GlasereiKessler</li>
    </ul>
  </div>
  <div class="glass" style="left:453px;top:59px"></div>
  <div class="brand-tile" style="left:480px;top:80px">
    <p class="brand-name">Glaserei<br>Kessler</p>
  </div>
</section>

<!-- Innenseite -->
<h2 class="section-title" style="top:404px">Innenseite</h2>
<section class="sheet inside">
  <div class="panel" style="left:0;width:125px;background:var(--stone)">
    <h1 class="title-light abs" style="left:13px;top:54px">Glaserei Kessler</h1>
    <div class="body-copy abs" style="left:13px;top:89px;width:102px">
      <p>Lorem ipsum dolor sit amet, consectetuer adipiscing elit, sed diam nonummy nibh euismod tincidunt ut laoreet dolore magna aliquam erat volutpat. Ut wisi enim ad minim veniam, quis nostrud exerci tation ullamcorper suscipit lobortis nisl ut aliquip ex ea commodo consequat.</p>
      <p style="margin-top:8px">Duis autem vel eum iriure dolor in hendrerit in vulputate velit esse molestie consequat, vel illum dolore eu feugiat nulla facilisis at vero eros et accumsan et iusto odio dignissim qui blandit praesent luptatum zzril delenit augue duis dolore te feugait nulla facilisi.<br>Lorem ipsum dolor sit amet, cons ectetuer adipiscing elit, sed diam nonummy nibh</p>
    </div>
  </div>
  <div class="panel" style="left:125px;width:82px;background:var(--dark)">
    <div class="photo abs" role="img" aria-label="Porträtfoto des Geschäftsführers" style="left:15px;top:58px;width:67px;height:88px"></div>
    <p class="caption abs" style="right:6px;top:153px">Lars-Martin Kessler<br>Geschäftsführer</p>
    <div class="contact" style="left:6px;top:214px">
      <h3>Kontaktdaten</h3>
      <ul>
        <li><svg><use href="#i-pin"/></svg>Lindenweg 12, 22145 Nordstadt</li>
        <li><svg><use href="#i-globe"/></svg>info@glaserei-kessler.de</li>
        <li><svg><use href="#i-mail"/></svg>www.glaserei-kessler.de</li>
        <li><svg><use href="#i-square"/></svg>XXX Glaserei Kessler</li>
        <li><svg><use href="#i-circle"/></svg>www.netzprofil.de/GlasereiKessler</li>
      </ul>
    </div>
  </div>
  <div class="panel" style="left:207px;width:208px;background:var(--white)"></div>
  <div class="panel" style="left:415px;width:208px;background:var(--stone)">
    <p class="vertical-word" style="left:163px;top:20px;height:250px;font-size:43px;color:var(--stripe);text-align:left">Glaserei Kessler</p>
  </div>
</section>

<!-- Innenseite Alternative -->
<h2 class="section-title" style="top:799px;left:30px">Innenseite- Alternative</h2>
<section class="sheet alt">
  <svg class="abs" style="left:0;top:0" width="623" height="290" aria-hidden="true">
    <line x1="96" y1="14" x2="16" y2="96" stroke="#111" stroke-width=".6"/>
    <line x1="412" y1="0" x2="412" y2="237" stroke="#e6e3e0" stroke-width=".8"/>
  </svg>
  <h1 class="title-bold abs" style="left:15px;top:18px">Glaserei<br>Kessler</h1>
  <p class="body-copy abs" style="left:70px;top:56px;width:122px">Lorem ipsum dolor sit amet, consectetuer adipiscing elit, sed diam nonummy nibh euismod tincidunt ut laoreet dolore magna aliquam erat volutpat. Ut wisi enim ad minim veniam, quis nostrud exerci tation ullamcorper suscipit lobortis nisl ut aliquip ex ea commodo consequat. Duis autem vel eum iriure dolor in hendrerit in vulputate velit esse molestie consequat, vel illum dolore eu feugiat nulla facilisis at vero eros et accumsan et iusto odio dignissim qui blandit praesent luptatum zzril delenit augue duis dolore te feugait nulla facilisi.</p>
  <div class="abs" style="left:0;top:183px;width:139px;height:107px;background:var(--stone)"></div>
  <div class="contact">
    <h3>Kontaktdaten</h3>
    <ul>
      <li><svg><use href="#i-pin"/></svg>Lindenweg 12, 22145 Nordstadt</li>
      <li><svg><use href="#i-globe"/></svg>info@glaserei-kessler.de</li>
      <li><svg><use href="#i-mail"/></svg>www.glaserei-kessler.de</li>
      <li><svg><use href="#i-square"/></svg>XXX Glaserei Kessler</li>
      <li><svg><use href="#i-circle"/></svg>www.netzprofil.de/GlasereiKessler</li>
    </ul>
  </div>
  <div class="photo abs" role="img" aria-label="Porträtfoto des Geschäftsführers" style="left:139px;top:183px;width:67px;height:87px;background:linear-gradient(160deg,#c8c9cb 0%,#6b6d70 40%,#1a1a1d 100%)"></div>
  <p class="name-plate" style="left:139px;top:270px;width:67px;height:20px">Lars-Martin Kessler<br>Geschäftsführer</p>
  <p class="vertical-word" style="left:582px;top:34px;height:245px;font-size:44px;color:var(--ghost);text-align:left">Glaserei Kessler</p>
</section>

</body>
</html>
```